Business Card Design Project

We need a business card for our new business based in Vancouver called
"Lumora Rest Spa" We are looking for a simple yet bold design for our business cards that will enable us to stand out from the pack. All business card details will be provided in the handover stage.
Updates

Thank you to all who have submitted

The work is great for the most part
Cards with creative use of the logo
have been more successful so far

Dark cards and rounded edges 
are also getting good reviews

Double sided is an option we would like to see explored

Thank you

Target Market(s)

Our clients are stressed business people, yoga/meditation enthusiast, and people looking for a new experience in a Spa enviroment

Industry/Entity Type

Business

Font styles to use
Other font styles liked:
• please check design file

Requirements
Must have
• Lumora Rest Spa

5218 E Kestrel Row, Vancouver, BC V5N 4K7

lumora@calmhaven.ca
Nice to have
• Creative approach to layout and design

Outside of the box design elements
Should not have
• Should not be too busy

```html
<!DOCTYPE html>
<html lang="en">
<head>
<meta charset="utf-8">
<title>Lumora Rest Spa — Business Cards</title>
<link rel="stylesheet" href="https://fonts.googleapis.com/css2?family=Ubuntu:wght@400&display=swap">
<style>
  :root {
    --page: #ffffff;
    --navy-deep: #05052a;
    --navy: #0c0c5c;
    --blue: #1818d8;
    --blue-bright: #2a2aff;
    --ink-light: #e6e8ff;
    --brand: #b9bfff;
    --edge: #3a3a8a;
  }
  * { box-sizing: border-box; margin: 0; padding: 0; }
  html, body {
    width: 999px; height: 1200px; overflow: hidden;
    background: var(--page);
    font-family: "Ubuntu", sans-serif;
  }
  .sheet { position: relative; width: 999px; height: 1200px; }

  .card {
    position: absolute;
    border-radius: 22px;
    border: 1px solid var(--edge);
    overflow: hidden;
    color: var(--ink-light);
  }
  .card-bg { position: absolute; inset: 0; }
  .card--landscape .card-bg {
    background:
      radial-gradient(ellipse 120% 70% at 70% 120%, var(--blue-bright) 0%, rgba(42,42,255,0) 70%),
      linear-gradient(160deg, var(--navy-deep) 0%, var(--navy) 45%, var(--blue) 100%);
  }
  .card--portrait .card-bg {
    background:
      linear-gradient(180deg, var(--navy-deep) 0%, var(--navy-deep) 55%, var(--navy) 72%, var(--blue-bright) 100%);
  }
  .card--portrait.card--lit .card-bg {
    background:
      radial-gradient(ellipse 120% 60% at 50% 115%, var(--blue-bright) 0%, rgba(42,42,255,0) 70%),
      linear-gradient(180deg, var(--navy) 0%, #10106e 50%, var(--blue) 100%);
  }

  .brand {
    position: absolute;
    left: 0; right: 0;
    display: flex; align-items: center; justify-content: center;
    color: var(--brand);
    font-weight: 400;
    white-space: nowrap;
  }
  .brand-dot {
    border-radius: 50%;
    background: var(--brand);
    flex: none;
  }

  .contact { position: absolute; }

  .card--landscape { width: 589px; height: 371px; left: 0; }
  .card--landscape .brand { top: 134px; font-size: 50px; gap: 18px; }
  .card--landscape .brand-dot { width: 26px; height: 26px; }
  .card--landscape .contact {
    left: 0; right: 0; top: 284px;
    text-align: center; font-size: 19px; line-height: 30px;
  }

  .card--portrait { width: 367px; left: 631px; }
  .card--portrait .brand { font-size: 36px; gap: 14px; }
  .card--portrait .brand-dot { width: 18px; height: 18px; }
  .card--portrait .contact {
    left: 32px; font-size: 21px; line-height: 27px;
  }
  .card--portrait .contact-email { margin-top: 24px; }

  .card-a { top: 106px; }
  .card-b { top: 619px; }
  .card-c { top: 0; height: 585px; }
  .card-c .brand { top: 236px; }
  .card-c .contact { top: 426px; }
  .card-d { top: 611px; height: 589px; }
  .card-d .brand { top: 234px; }
  .card-d .contact { top: 430px; }
</style>
</head>
<body>
<main class="sheet">

  <section class="card card--landscape card-a">
    <div class="card-bg" role="img" aria-label="Deep navy to bright blue gradient with faint flowing line pattern"></div>
    <div class="brand"><span class="brand-dot"></span>Lumora Rest Spa</div>
    <div class="contact">
      <p>5218 E Kestrel Row, Vancouver, BC V5N 4K7</p>
      <p>lumora@calmhaven.ca</p>
    </div>
  </section>

  <section class="card card--landscape card-b">
    <div class="card-bg" role="img" aria-label="Deep navy to bright blue gradient with faint flowing line pattern"></div>
    <div class="brand"><span class="brand-dot"></span>Lumora Rest Spa</div>
    <div class="contact">
      <p>5218 E Kestrel Row, Vancouver, BC V5N 4K7</p>
      <p>lumora@calmhaven.ca</p>
    </div>
  </section>

  <section class="card card--portrait card-c">
    <div class="card-bg" role="img" aria-label="Dark navy gradient glowing blue at the base with faint flowing line pattern"></div>
    <div class="brand"><span class="brand-dot"></span>Lumora Rest Spa</div>
    <div class="contact">
      <p>5218 E Kestrel Row</p>
      <p>Vancouver</p>
      <p>BC V5N 4K7</p>
      <p class="contact-email">lumora@calmhaven.ca</p>
    </div>
  </section>

  <section class="card card--portrait card--lit card-d">
    <div class="card-bg" role="img" aria-label="Navy to bright blue gradient with faint flowing line pattern"></div>
    <div class="brand"><span class="brand-dot"></span>Lumora Rest Spa</div>
    <div class="contact">
      <p>5218 E Kestrel Row</p>
      <p>Vancouver</p>
      <p>BC V5N 4K7</p>
      <p class="contact-email">lumora@calmhaven.ca</p>
    </div>
  </section>

</main>
</body>
</html>
```